BrightHarbor is a fund management company that takes just four market positions a year. each position is linked to a big geopolitical and economic event happening in the world. So for example we may be buying gold mining stocks-these are the companies who dig the gold out of the ground, as all the gold is currently being bought by Asia, or buying the japanese stock market as this is one of the big stories of today.

I am looking for a logo that represents 'BrightHarbor'-the Bright Harbor.

I would like it to be small and sit to the left of the name of the company on the left hand side(I think!)on the top line of the business card please.

Industry/Entity Type

Mining

Contact Information for Business Card

BrightHarbor Investment management Ltd
41 Fennick Lane
London E9 7QT

Tomas P Hulme

Mob: 0(44)7839254086
Off: 0(44) 203 xxxx
email: th@brightharbor-fm.example

```html
<!DOCTYPE html>
<html lang="en">
<head>
<meta charset="utf-8">
<title>BrightHarbor Investment management Ltd – Business Card</title>
<link rel="stylesheet" href="https://fonts.googleapis.com/css2?family=Tinos&display=swap">
<style>
  :root {
    --card-bg: #ffffff;
    --ink-navy: #10106a;
  }
  html, body {
    margin: 0;
    padding: 0;
    overflow: hidden;
    background: var(--card-bg);
  }
  .business-card {
    position: relative;
    width: 1200px;
    height: 800px;
    background: var(--card-bg);
    color: var(--ink-navy);
    font-family: "Tinos", "Times New Roman", serif;
    overflow: hidden;
  }
  .brand-mark {
    position: absolute;
    left: 152px;
    top: 262px;
    width: 72px;
    height: 72px;
    border-radius: 50%;
    background: var(--ink-navy);
  }
  .company-name {
    position: absolute;
    left: 243px;
    top: 288px;
    margin: 0;
    font-size: 40px;
    font-weight: 400;
    line-height: 1;
    white-space: nowrap;
  }
  .contact-block {
    position: absolute;
    left: 147px;
    margin: 0;
    font-size: 30px;
    line-height: 41px;
    font-style: normal;
    white-space: nowrap;
  }
  .postal-address { top: 446px; }
  .person-details { top: 562px; }
</style>
</head>
<body>
  <main class="business-card">
    <span class="brand-mark" aria-hidden="true"></span>
    <h1 class="company-name">BrightHarbor Investment management Ltd</h1>

    <address class="contact-block postal-address">
      41 Fennick Lane<br>
      London E9 7QT
    </address>

    <address class="contact-block person-details">
      Tomas P Hulme<br>
      Mob: 0(44)7839254086<br>
      Off: 0(44) 203 xxxx<br>
      email: th@brightharbor-fm.example
    </address>
  </main>
</body>
</html>
```